Design Tweak needed for a current site

Design on top of an existing quiz funnel

Ideally we would like to tweak what we have already built here (moving elements, styles, adding simple elements etc): http://offers.rateplumfinder.com/could-you-cut-your-auto-premium

The flow:
1) User lands on the quiz page
2) User answers X questions and moves through the flow
3) Calculating user results screen
4) User reaches a success screen, and is subsequently redirected

Keys to the design:
1) We need to emphasize the quiz title as that will drive engagement. In this case, this is a quiz to see if you might be eligible to save money on car insurance.

2) At the end of the quiz we need to make it very, very clear that the user is eligible for savings and that in order to complete the process they are being redirected to another page where they need to fill out a form. It is critical that the design communicates this very clearly... We can count down the time left until redirect and we can use any order of elements to make this point. I think our current design does a very bad job of this.

3) We want to have a "calculating" step so that it seems like the page is working in the background

Goals of the design:
1) Polished, high quality experience throughout
2) User is clearly prepared to be redirected to the conversion funnel/landing page at the end
3) User understands the value of completing the quiz

Target Market(s)

designers

Industry/Entity Type

Moving

Number of Pages Required

1 page

Font styles to use
Sans Serif

Colors

Designer to choose colors to be used in the design.

Requirements
Must have
• This quiz funnel is a template so while the current use case is for auto insurance, we would like a design that also would work in other contexts.
Should not have
• We don't want to materially change the core functionality of the quiz itself... redesigning any of the elements or interactions is encouraged though

```html
<!DOCTYPE html>
<html lang="en">
<head>
<meta charset="utf-8">
<title>RatePlumFinder Quiz</title>
<link href="https://fonts.googleapis.com/css2?family=Poppins:wght@400;500;600;700&display=swap" rel="stylesheet">
<style>
:root{
  --bg-light:#ececec;
  --bg-dark:#d6d6d6;
  --card:#ffffff;
  --ink:#222222;
  --text:#444444;
  --muted:#666666;
  --pill:#7b7b7b;
  --ring:#d9d9d9;
  --ring-edge:#c8c8c8;
  --track:#f4f4f4;
  --green:#7cb518;
  --green-dark:#5e9a0c;
  --faint:#dcdcdc;
  --icon-area:#d4d4d4;
}
*{box-sizing:border-box;margin:0;padding:0}
html,body{width:1200px;height:771px;overflow:hidden}
body{
  font-family:"Poppins",sans-serif;
  background:radial-gradient(ellipse at 50% 40%,var(--bg-light) 0%,var(--bg-dark) 100%);
  position:relative;color:var(--text);
}
.bg-vehicle{position:absolute;background:var(--faint);opacity:.55;border-radius:14px 22px 6px 6px}
.brand-tab{
  position:absolute;left:366px;top:39px;width:459px;height:78px;
  background:linear-gradient(#ffffff,#f2f2f2);
  clip-path:polygon(3% 0,97% 0,100% 100%,0 100%);
  border-radius:10px 10px 0 0;
}
.brand{
  position:absolute;left:0;right:0;top:56px;display:flex;justify-content:center;align-items:center;gap:9px;
  font-size:33px;font-weight:500;color:var(--ink);letter-spacing:.3px;
}
.brand-dot{width:30px;height:30px;border-radius:50%;background:var(--ink)}
.quiz-card{
  position:absolute;left:165px;top:117px;width:861px;height:611px;background:var(--card);
  border-radius:4px;box-shadow:0 2px 14px rgba(0,0,0,.06);
}
.deco-marks{position:absolute;background:linear-gradient(90deg,#e4e4e4,#efefef);border-radius:20px;opacity:.8}
.quiz-bubble{position:absolute;left:371px;top:53px;width:128px;height:38px}
.quiz-bubble span{
  position:absolute;inset:0;display:flex;align-items:center;justify-content:center;
  font-size:24px;font-weight:700;color:var(--ink);letter-spacing:.5px;
}
.quiz-title{position:absolute;left:0;right:0;top:122px;text-align:center;font-size:24px;font-weight:400;color:var(--text)}
.quiz-intro{
  position:absolute;left:93px;top:194px;width:685px;height:32px;background:var(--pill);border-radius:5px;
  color:#fff;font-size:14.5px;font-weight:500;display:flex;align-items:center;justify-content:center;
}
.step-tab{
  position:absolute;left:345px;top:256px;width:182px;height:36px;background:#ececec;
  clip-path:polygon(10% 0,90% 0,100% 100%,0 100%);border-radius:8px 8px 0 0;
  font-size:16px;color:var(--muted);display:flex;align-items:center;justify-content:center;padding-top:3px;
}
.progress{
  position:absolute;left:29px;top:291px;width:813px;height:34px;border-radius:17px;
  background:linear-gradient(#ffffff,var(--track));border:3px solid #dedede;
}
.progress-fill{
  position:absolute;left:4px;top:4px;width:147px;height:20px;border-radius:10px;
  background:repeating-linear-gradient(135deg,var(--green) 0 2px,var(--green-dark) 2px 3px);
}
.question{position:absolute;left:0;right:0;top:348px;text-align:center;font-size:20.5px;font-weight:400;color:var(--text)}
.choice{position:absolute;top:400px;width:144px;text-align:center;text-decoration:none;color:var(--text)}
.choice-ring{
  width:144px;height:144px;border-radius:50%;background:var(--ring);border:2px solid var(--ring-edge);
  display:flex;align-items:center;justify-content:center;
}
.choice-core{
  width:118px;height:118px;border-radius:50%;background:linear-gradient(#ffffff,#ececec);
  display:flex;align-items:center;justify-content:center;box-shadow:0 1px 3px rgba(0,0,0,.12);
}
.choice-icon{width:64px;height:56px;border-radius:8px;background:linear-gradient(var(--icon-area),#e2e2e2)}
.choice-label{display:block;margin-top:9px;font-size:20px;letter-spacing:.5px}
.choice--lease{left:274px}
.choice--own{left:451px}
</style>
</head>
<body>
  <div class="bg-vehicle" style="left:170px;top:80px;width:130px;height:34px" role="img" aria-label="Faint car outline decoration"></div>
  <div class="bg-vehicle" style="left:943px;top:78px;width:88px;height:36px" role="img" aria-label="Faint SUV outline decoration"></div>
  <div class="bg-vehicle" style="left:90px;top:567px;width:75px;height:40px" role="img" aria-label="Faint car outline decoration"></div>
  <div class="bg-vehicle" style="left:175px;top:730px;width:208px;height:38px" role="img" aria-label="Faint pair of cars outline decoration"></div>
  <div class="bg-vehicle" style="left:988px;top:715px;width:103px;height:44px" role="img" aria-label="Faint pickup outline decoration"></div>

  <div class="brand-tab"></div>
  <div class="brand"><span class="brand-dot"></span><span>RatePlumFinder</span></div>

  <main class="quiz-card">
    <div class="deco-marks" style="left:264px;top:17px;width:102px;height:64px" role="img" aria-label="Cluster of grey question marks"></div>
    <div class="deco-marks" style="left:492px;top:16px;width:101px;height:64px" role="img" aria-label="Cluster of grey question marks"></div>

    <div class="quiz-bubble">
      <svg width="128" height="56" viewBox="0 0 128 56">
        <path d="M19 1.5H109a17.5 17.5 0 0 1 0 35H80L69 55 60 36.5H19a17.5 17.5 0 0 1 0-35z" fill="#f3f3f3" stroke="#cfcfcf" stroke-width="2"/>
      </svg>
      <span style="height:38px">QUIZ</span>
    </div>

    <h1 class="quiz-title">Are You Overpaying For Car Insurance?</h1>
    <p class="quiz-intro">Take our five question quiz to see if you might be eligible for car insurance savings</p>

    <div class="step-tab">Question 1/2</div>
    <div class="progress"><div class="progress-fill"></div></div>

    <h2 class="question">Do you Lease Or Own:</h2>

    <a class="choice choice--lease" href="#">
      <span class="choice-ring"><span class="choice-core">
        <span class="choice-icon" role="img" aria-label="Lease agreement pictogram"></span>
      </span></span>
      <span class="choice-label">I Lease!</span>
    </a>

    <a class="choice choice--own" href="#">
      <span class="choice-ring"><span class="choice-core">
        <span class="choice-icon" role="img" aria-label="Owned vehicle pictogram"></span>
      </span></span>
      <span class="choice-label">I Own!</span>
    </a>
  </main>
</body>
</html>
```